I'm an Executive Coach. I need a cover for a leadership book.

Title: Quiet Compass Steady Course Guidance from the Center of the Soul. The focus in my work "Spirit Kindled Reach" I use a lot of fire and heart-centered frame work and imagery. The book should have a leadership presence with an inspirational feel. The purpose is to invite really smart leaders to pay attention and to lead from their heart so they can have great impact in the work they do and the lives they live. paxtonlowry.example to see site branding, colors. Author: Paxton Lowry

Target Market(s)

The audience is those lead others from the manager level to the executive level and entrepreneurs starting and leading their own companies They are usually trailblazers, care about connecting with people as they lead. The big message is being confifent to lead ftom values, intention and from what matters most.

Industry/Entity Type

Executive coaching

Font styles to use
Serif

Requirements
Must have
• Lighter feel. Perhaps avoid a total black background.
Nice to have
• While it is a leadership book, i would like it to feel creative and inviting not authoritative.
Should not have
• Dark colors as the main color

```html
<!DOCTYPE html>
<html lang="en">
<head>
<meta charset="utf-8">
<title>Quiet Compass Steady Course — Paxton Lowry</title>
<link rel="stylesheet" href="https://fonts.googleapis.com/css2?family=Teko:wght@400;500;600&family=Parisienne&display=swap">
<style>
  :root {
    --bg-light: #c6dfe2;
    --bg-mid: #a9c9cd;
    --bg-deep: #8fb3b8;
    --title-red: #a51f27;
    --subtitle-slate: #36454f;
    --author-red: #b3262e;
    --art-light: #b5d0d3;
    --art-mid: #7fa5aa;
    --art-accent: #c2362c;
  }
  * { margin: 0; padding: 0; box-sizing: border-box; }
  html, body { width: 800px; height: 1200px; overflow: hidden; }
  body { background: var(--bg-mid); }
  .cover {
    position: relative;
    width: 800px;
    height: 1200px;
    overflow: hidden;
    background: linear-gradient(120deg, var(--bg-light) 0%, var(--bg-mid) 55%, var(--bg-deep) 100%);
  }
  .book-title {
    position: absolute;
    top: 52px;
    left: 0;
    width: 800px;
    text-align: center;
    font-family: "Teko", "Arial Narrow", sans-serif;
    font-weight: 500;
    font-size: 178px;
    line-height: 138px;
    color: var(--title-red);
    text-transform: uppercase;
    letter-spacing: 2px;
  }
  .book-title span { display: block; height: 138px; }
  .book-subtitle {
    position: absolute;
    top: 600px;
    left: 0;
    width: 800px;
    text-align: center;
    font-family: "Teko", "Arial Narrow", sans-serif;
    font-weight: 500;
    font-size: 43px;
    line-height: 50px;
    letter-spacing: 1.5px;
    color: var(--subtitle-slate);
    text-transform: uppercase;
  }
  .cover-art {
    position: absolute;
    top: 720px;
    left: 0;
    width: 800px;
    height: 300px;
  }
  .author-name {
    position: absolute;
    top: 1085px;
    left: 0;
    width: 800px;
    text-align: center;
    font-family: "Parisienne", cursive;
    font-size: 74px;
    line-height: 1;
    color: var(--author-red);
  }
</style>
</head>
<body>
  <main class="cover">
    <h1 class="book-title">
      <span>Quiet</span>
      <span>Compass</span>
      <span>Steady</span>
      <span>Course</span>
    </h1>
    <p class="book-subtitle">Personal &amp; Professional Guidance<br>from the Center of the Soul</p>

    <svg class="cover-art" viewBox="0 0 800 300" role="img" aria-label="Illustration of three square icon frames on a reflective shelf, the centre one red with a glowing white heart, flanked by two pale teal frames with embossed hearts">
      <defs>
        <linearGradient id="art-shelf" x1="0" y1="0" x2="0" y2="1">
          <stop offset="0" stop-color="var(--art-light)" stop-opacity="0"/>
          <stop offset="0.5" stop-color="var(--art-mid)" stop-opacity="0.55"/>
          <stop offset="1" stop-color="var(--art-light)" stop-opacity="0.2"/>
        </linearGradient>
        <radialGradient id="art-glow" cx="0.5" cy="0.42" r="0.5">
          <stop offset="0" stop-color="var(--art-accent)" stop-opacity="0.75"/>
          <stop offset="1" stop-color="var(--art-accent)" stop-opacity="0"/>
        </radialGradient>
      </defs>
      <rect x="0" y="0" width="800" height="300" fill="url(#art-shelf)"/>
      <rect x="250" y="0" width="300" height="260" fill="url(#art-glow)"/>
    </svg>

    <p class="author-name">Paxton Lowry</p>
  </main>
</body>
</html>
```